Marlow Creek Nectar Company, local Honey producer needs product Lable to encourage sales

We are a small business (Marlow Creek Nectar Company) located in a small Texas town that harvests honey from our beehives yearly. Our honey would be considered "raw wildflower honey" and our goal is to sell it locally (farmers markets) and to surrounding areas.

We are currently packaging in plastic classic honey bottles with white flip caps. Sizes are 8oz and 16oz bottles (see pictures for actual size). Larger orders will be filled in one quart mason jars.

Design Ideas:
-vintage style design with bee or several bees in background
- incorporate company name "Marlow Creek Nectar Company"
- needs small description "Raw Honey", and "Harvested in Bellville, Texas"

Target Market(s)

Farmers markets, health conscience people looking for unprocessed food options

Industry/Entity Type

Small Business

Requirements
Nice to have
• Vintage feel
Should not have
• No cartoonish characters

```html
<!DOCTYPE html>
<html lang="en">
<head>
<meta charset="utf-8">
<title>Marlow Creek Nectar Company – Raw Honey Label</title>
<link rel="stylesheet" href="https://fonts.googleapis.com/css2?family=Playfair+Display:wght@400;700&display=swap">
<style>
  :root {
    --page-bg: #f3ead9;
    --label-orange: #f07c1e;
    --label-orange-light: #f6a24a;
    --label-outline: #1a1008;
    --ink-dark: #2b1406;
    --comb-light: #f2c25a;
    --comb-deep: #d98a1c;
  }
  * { margin: 0; padding: 0; box-sizing: border-box; }
  html, body {
    width: 1200px;
    height: 1200px;
    overflow: hidden;
    background: var(--page-bg);
  }
  .canvas {
    position: relative;
    width: 1200px;
    height: 1200px;
  }
  .label {
    position: absolute;
    left: 290px;
    top: 100px;
    width: 620px;
    height: 1000px;
    border: 4px solid var(--label-outline);
    border-radius: 50% / 31%;
    background: linear-gradient(160deg, var(--label-orange) 0%, var(--label-orange) 45%, var(--label-orange-light) 100%);
    overflow: hidden;
    font-family: "Playfair Display", serif;
    color: var(--ink-dark);
    text-align: center;
  }
  .brand-name {
    position: absolute;
    left: 0;
    right: 0;
    top: 150px;
    font-weight: 700;
    font-size: 66px;
    line-height: 1.05;
  }
  .product-type {
    position: absolute;
    left: 0;
    right: 0;
    top: 385px;
    font-weight: 400;
    font-size: 70px;
    letter-spacing: -1px;
  }
  .origin {
    position: absolute;
    left: 0;
    right: 0;
    top: 478px;
    font-weight: 400;
    font-size: 40px;
  }
  .comb-art {
    position: absolute;
    left: 40px;
    top: 545px;
    width: 560px;
    height: 380px;
    border-radius: 0 0 48% 48% / 0 0 40% 40%;
    background: radial-gradient(ellipse at 65% 55%, var(--comb-light) 0%, var(--comb-deep) 70%, rgba(217,138,28,0) 100%);
    opacity: 0.9;
  }
  .net-weight {
    position: absolute;
    left: 0;
    right: 0;
    top: 915px;
    font-weight: 400;
    font-size: 30px;
  }
</style>
</head>
<body>
  <main class="canvas">
    <section class="label">
      <h1 class="brand-name">Marlow Creek<br>Nectar Company</h1>
      <p class="product-type">RAW HONEY</p>
      <p class="origin">Harvested in Bellville, Texas</p>
      <div class="comb-art" role="img" aria-label="Illustration of golden honeycomb cells with a honeybee resting on them"></div>
      <p class="net-weight">8 OZ./ 227 GR</p>
    </section>
  </main>
</body>
</html>
```